Create Lanternfield HR Business Cards.

Create Business Cards for Lanternfield HR. 2 sided and Would like the back to have the logo.

Info for Business Card:
Address: 4827 Millbrook Ave Suite 230 Cleveland, Ohio 44987
Office Number: 216-555-0143
Mobile: 216-555-0192

Website: www.lanternfieldhr.example

Target Market(s)

Small to medium size businesses

Industry/Entity Type

Human Resources

Contact Information for Business Card

Company logo and information

Font styles to use
Serif
Sans Serif

Requirements
Must have
• Info for Business Card: Address: 4827 Millbrook Ave Suite 230 Cleveland, Ohio 44987 Office Number: 216-555-0143 Mobile: 216-555-0192 Website: www.lanternfieldhr.example

```html
<!DOCTYPE html>
<html lang="en">
<head>
<meta charset="utf-8">
<title>Lanternfield HR – Business Cards</title>
<link href="https://fonts.googleapis.com/css2?family=Montserrat:wght@500;800&display=swap" rel="stylesheet">
<style>
  :root {
    --navy: #2a2460;
    --orange: #f48a22;
    --white: #ffffff;
    --ink: #1b1b1f;
    --stage: #e9e9ec;
  }
  * { box-sizing: border-box; margin: 0; padding: 0; }
  html, body { width: 1200px; height: 900px; overflow: hidden; }
  body {
    background: var(--stage);
    font-family: "Montserrat", Arial, sans-serif;
    display: flex;
    flex-direction: column;
    align-items: center;
    justify-content: center;
    gap: 40px;
  }
  .card {
    position: relative;
    width: 700px;
    height: 400px;
    overflow: hidden;
    box-shadow: 0 6px 20px rgba(0,0,0,.18);
  }
  .card--front { background: var(--white); }
  .card--back { background: var(--navy); display: flex; align-items: center; justify-content: center; }

  .card__wave { position: absolute; inset: 0; width: 100%; height: 100%; }

  .brand {
    position: absolute;
    display: flex;
    align-items: center;
    gap: 12px;
    font-weight: 800;
    letter-spacing: .5px;
  }
  .brand__dot { width: 30px; height: 30px; border-radius: 50%; background: var(--orange); flex: none; }
  .card--front .brand { left: 40px; top: 110px; font-size: 26px; color: var(--navy); }
  .card--back .brand { position: static; font-size: 44px; color: var(--white); }
  .card--back .brand__dot { width: 46px; height: 46px; }

  .card__divider {
    position: absolute;
    left: 318px; top: 60px;
    width: 2px; height: 170px;
    background: var(--orange);
  }

  .contact {
    position: absolute;
    left: 340px; top: 62px;
    color: var(--ink);
    font-weight: 500;
    font-size: 15px;
    line-height: 1.45;
  }
  .contact__name {
    color: var(--orange);
    font-weight: 800;
    font-size: 17px;
    letter-spacing: .5px;
    text-transform: uppercase;
    margin-bottom: 2px;
  }
  .contact__address { margin-bottom: 8px; }
  .contact__row { display: flex; align-items: center; gap: 9px; }
  .contact__icon { width: 15px; height: 15px; fill: var(--orange); flex: none; }
</style>
</head>
<body>

<section class="card card--front" aria-label="Business card front">
  <svg class="card__wave" viewBox="0 0 700 400" preserveAspectRatio="none" aria-hidden="true">
    <path d="M0,120 C8,270 200,300 400,330 C500,345 545,365 565,400 L0,400 Z" fill="#2a2460"/>
    <path d="M30,205 C100,300 300,305 420,330 C495,345 530,358 545,380" fill="none" stroke="#f48a22" stroke-width="3"/>
  </svg>

  <div class="brand"><span class="brand__dot"></span>Lanternfield HR</div>

  <div class="card__divider"></div>

  <div class="contact">
    <p class="contact__name">Lanternfield HR</p>
    <p class="contact__address">4827 Millbrook Ave Suite 230<br>Cleveland, Ohio 44987</p>
    <p class="contact__row">
      <svg class="contact__icon" viewBox="0 0 24 24" aria-hidden="true"><path d="M6.6 10.8a15 15 0 0 0 6.6 6.6l2.2-2.2c.3-.3.7-.4 1-.2 1.1.4 2.3.6 3.6.6.6 0 1 .4 1 1V20c0 .6-.4 1-1 1A17 17 0 0 1 3 4c0-.6.4-1 1-1h3.5c.6 0 1 .4 1 1 0 1.3.2 2.5.6 3.6.1.3 0 .7-.2 1z"/></svg>
      216-555-0143
    </p>
    <p class="contact__row">
      <svg class="contact__icon" viewBox="0 0 24 24" aria-hidden="true"><path d="M7 1h10a2 2 0 0 1 2 2v18a2 2 0 0 1-2 2H7a2 2 0 0 1-2-2V3a2 2 0 0 1 2-2zm0 3v14h10V4zm5 15.5a1 1 0 1 0 0 2 1 1 0 0 0 0-2z"/></svg>
      216-555-0192
    </p>
    <p class="contact__row">
      <svg class="contact__icon" viewBox="0 0 24 24" aria-hidden="true"><path d="M2 5h20v14H2zm2 2v.5l8 5 8-5V7zm0 2.8V17h16V9.8l-8 5z"/></svg>
      info@lanternfieldhr.example
    </p>
    <p class="contact__row">
      <svg class="contact__icon" viewBox="0 0 24 24" aria-hidden="true"><path d="M12 2a10 10 0 1 0 0 20 10 10 0 0 0 0-20zm6.9 6h-3a15 15 0 0 0-1.3-3.9A8 8 0 0 1 18.9 8zM12 4c.8 1.2 1.5 2.5 1.9 4h-3.8c.4-1.5 1.1-2.8 1.9-4zM4.3 14a8 8 0 0 1 0-4h3.4a16 16 0 0 0 0 4zm.8 2h3a15 15 0 0 0 1.3 3.9A8 8 0 0 1 5.1 16zm3-8h-3a8 8 0 0 1 4.3-3.9C8.8 5.3 8.4 6.6 8.1 8zM12 20c-.8-1.2-1.5-2.5-1.9-4h3.8c-.4 1.5-1.1 2.8-1.9 4zm2.3-6H9.7a14 14 0 0 1 0-4h4.6a14 14 0 0 1 0 4zm.3 5.9c.6-1.2 1-2.5 1.3-3.9h3a8 8 0 0 1-4.3 3.9zm1.7-5.9a16 16 0 0 0 0-4h3.4a8 8 0 0 1 0 4z"/></svg>
      www.lanternfieldhr.example
    </p>
  </div>
</section>

<section class="card card--back" aria-label="Business card back">
  <div class="brand"><span class="brand__dot"></span>Lanternfield HR</div>
</section>

</body>
</html>
```